Insect-based foods company needs bright, eye catching pouch design for its Green Flour Blend

We are a UK based cricket farm called Molten Acre (www.moltenacre-example.com) and have a retail brand called 'Hoplume' (www.hoplume-example.com). Our main product is 'Green Flour Blend' which we already sell wholesale, through the Hoplume website and on Tradevo UK. At the moment we have designed our own labels which we stick on stand up pouches. This does not look very professional and is very time consuming to do. We are looking to have our pouches custom printed instead and want a new, bold design. We want a design that is bright, colourful, and eye-catching. Our packaging needs to stand out and make the statement - 'this is not an ordinary protein powder'. A few key points:
1. The pouches measure 130mm*225mm
2. We want to keep our existing 'Hoplume' logo
3. We need a design for the front and back. Please use our existing text for the basis of the back of the pack but change it as you see fit.
4. We would like the Union Jack flag to show prominently. Ours is the only cricket powder on the market which is made in the UK and we want to make a big deal about this.
5. The packaging needs to grab peoples attention on the shelf and also on the Tradevo search results page.
6. We intend to use the style of the packaging to re-design our website to match it. This means the theme of the packaging needs to translate well to the overall look of the website.

Target Market(s)

Younger people looking for exiting new protein powder which is sustainable and healthy. Would like to appeal to both men and women.

Font styles to use
Sans Serif

Requirements
Must have
• 1. The pouches measure 130mm*225mm
3. We need a design for the front and back.
4. We would like the Union Jack flag to show somewhere on the packaging. Ours is the only cricket powder on the market which is made in the UK and we want to make a big deal about this.

```html
<!DOCTYPE html>
<html lang="en">
<head>
<meta charset="utf-8">
<title>Hoplume – Green Flour Blend pouch</title>
<link rel="stylesheet" href="https://fonts.googleapis.com/css2?family=Oswald:wght@500;600&family=Nunito:wght@700&display=swap">
<style>
  :root {
    --bg: #ececec;
    --pouch-red: #d8262c;
    --pouch-red-deep: #c21a22;
    --gold: #f1c98c;
    --white: #ffffff;
    --flag-blue: #1f3a8a;
    --flag-red: #d22630;
  }
  * { margin: 0; padding: 0; box-sizing: border-box; }
  html, body {
    width: 1200px; height: 1164px; overflow: hidden;
    background: var(--bg);
  }
  .canvas { position: relative; width: 1200px; height: 1164px; }
  .pouch {
    position: absolute; left: 381px; top: 198px;
    width: 438px; height: 768px;
    background: linear-gradient(90deg, var(--pouch-red-deep) 0%, var(--pouch-red) 12%, var(--pouch-red) 88%, var(--pouch-red-deep) 100%);
    border-radius: 14px 14px 4px 4px;
    overflow: hidden;
    color: var(--white);
    font-family: "Oswald", "Arial Narrow", sans-serif;
  }
  .top-pattern { position: absolute; left: 0; top: 0; width: 438px; height: 290px; }
  .brand-name {
    position: absolute; left: 81px; top: 322px;
    font-family: "Nunito", Arial, sans-serif; font-weight: 700;
    font-size: 46px; line-height: 1; letter-spacing: -0.5px;
    color: var(--white);
  }
  .product-title {
    position: absolute; left: 80px; top: 389px;
    font-weight: 600; font-size: 90px; line-height: 82px;
    text-transform: uppercase; letter-spacing: -0.5px;
  }
  .product-title .accent { color: var(--gold); }
  .tagline {
    position: absolute; left: 87px; top: 641px;
    font-weight: 500; font-size: 30px; line-height: 1;
    letter-spacing: 0.2px; text-transform: uppercase;
  }
  .badge { position: absolute; left: 326px; top: 351px; width: 110px; height: 110px; }
  .origin { position: absolute; left: 113px; top: 692px; width: 56px; text-align: center; }
  .origin svg { display: block; width: 48px; height: 28px; margin: 0 auto 2px; }
  .origin-text { font-weight: 500; font-size: 14px; line-height: 14px; text-transform: uppercase; }
  .net-weight {
    position: absolute; left: 179px; top: 720px;
    font-weight: 600; font-size: 35px; line-height: 1;
  }
  .servings {
    position: absolute; left: 292px; top: 708px; width: 56px;
    text-align: center; font-weight: 500; font-size: 13px; line-height: 15px;
    text-transform: uppercase;
  }
</style>
</head>
<body>
<div class="canvas">
  <div class="pouch">
    <svg class="top-pattern" viewBox="0 0 438 290" role="img" aria-label="Striped red and cream pattern with cricket silhouettes">
      <defs>
        <linearGradient id="pattern-tone" x1="0" y1="0" x2="1" y2="0">
          <stop offset="0" stop-color="#e9827a"/>
          <stop offset="0.5" stop-color="#eb9580"/>
          <stop offset="1" stop-color="#e9827a"/>
        </linearGradient>
      </defs>
      <polygon points="0,0 438,0 438,165 219,290 0,170" fill="url(#pattern-tone)"/>
    </svg>

    <div class="brand-name">hoplume</div>

    <svg class="badge" viewBox="0 0 110 110" aria-label="Ultrafine roasted">
      <defs>
        <path id="badge-arc" d="M 14 55 A 41 41 0 1 1 84 84"/>
      </defs>
      <path d="M 86.1 86.1 A 44 44 0 0 1 11 55" fill="none" stroke="var(--gold)" stroke-width="2" stroke-dasharray="0.5 4" stroke-linecap="round"/>
      <circle cx="55" cy="55" r="31" fill="var(--gold)" role="img" aria-label="Cricket emblem"/>
      <text font-family="Oswald, sans-serif" font-weight="600" font-size="11.5" fill="var(--gold)" letter-spacing="0.4">
        <textPath href="#badge-arc" startOffset="12%">ULTRAFINE ROASTED</textPath>
      </text>
    </svg>

    <h1 class="product-title">Green<br><span class="accent">Flour</span><br>Blend</h1>
    <p class="tagline">Six-legged superfood</p>

    <div class="origin">
      <svg viewBox="0 0 60 30" aria-label="Union flag">
        <clipPath id="flag-clip"><rect width="60" height="30"/></clipPath>
        <g clip-path="url(#flag-clip)">
          <rect width="60" height="30" fill="var(--flag-blue)"/>
          <path d="M0,0 L60,30 M60,0 L0,30" stroke="#fff" stroke-width="6"/>
          <path d="M0,0 L60,30 M60,0 L0,30" stroke="var(--flag-red)" stroke-width="2"/>
          <path d="M30,0 V30 M0,15 H60" stroke="#fff" stroke-width="10"/>
          <path d="M30,0 V30 M0,15 H60" stroke="var(--flag-red)" stroke-width="6"/>
        </g>
      </svg>
      <div class="origin-text">Farmed<br>in the UK</div>
    </div>

    <div class="net-weight">100G ℮</div>
    <div class="servings">Approx.<br>10<br>Servings</div>
  </div>
</div>
</body>
</html>
```